Talvoro Web Design

We need a redesign of our current website www.talvoro-example.com

THIS IS A DESIGN STAGE ONLY

We have attached details of the whole project for your understanding only

We do not want to change our Logo but do want to have a more modern and intuitive feel to the site.

The first stage is the design but we are also looking for a coder to take the site to the next level

Talvoro has a current website that has been in operation for the past 6 years the design was based around the Saas self-service model and while functional does not meet Talvoro needs with regard to the new positioning.

We are happy to stay in Fendrix or will look at alternatives

The purpose of the redesign is to align the look and feel of the website to meet our current new brand position and to provide a access point for the delivery of new content from Blogs and white papers as well as a portal for information for our current users for gathering Tips and Tricks and access to additional resources to assist them to provide feedback and get support.

Talvoro is Australia's only PPM (Project and Portfolio Management) software provider that caters to the needs of project managers and C-level executives looking for insights into the alignment of resources to business strategy and investment decisions.

As companies gain maturity in PPM there is a need for innovation and management of change beyond just implementation of tools this is why Talvoro has evolved from being a SaaS to becoming a SwS (Software with Service) provider.

Talvoro is recognized as the tool of choice amongst program and project managers that is able to provide the user with an intuitive reliable interface that is capable of evolving and maturing to meet and exceed client requirements.

We are able to provide people at the coalface with tools that enable them to manage resources, scope, time sheeting, issues, changes and risk with excellent reporting functionality.

For C-level executives we are able to provide Business Intelligence (BI) functionality and reporting by integrating the PPM data with other business management systems such as ERP and CRM to provide a insight beyond pure PPM reporting.

We are able to provide Project Management insights from years of experience working with our clients in developing solutions that are inline with the evolution that comes with change.

Please feel free to email me on nigel.brask@talvoro-example.com if you require any further details. A Site map and a wire frame is available.

Competitor sites include

www.plonverk-example.com
www.surmoza-example.com
www.qarnitel-example.com
www.velubra-example.com
Updates

Hi All 

We are getting some great designs coming in and really appreciate all of your efforts.

Some feedback to you all is that we have a preference for cleaner designs that take into account comprehension ability. So reverse type to us looks good but doesnt always get the cut through.

We have to remember that this is a marketing site first and foremost so what we are looking for is the ability to engage with our audience and get them to start to explore. That is upto us to provide great content and what we want from the design is the ability to be be able to engage with our Audience.

For your consideration please review this info from our marketing plan

There are 3 main communication groups inthe sales process.

Users-        These are the peoplewho will be at the coal face inputting the data and using the product on adaily basis. It is key to provide them with an easy to use and functional toolthat is able to provide them with the information they are looking for easily andintuitively. They have the capacity to say yes and can push the sale decisionup the chain. They equally have the power to say No and stop the sales processin its tracks. They will have a opinion who or what they feel is the best ofbreed and will try to influence the process.

Users are split into two groups.

Group1- They will be diploma if not degree qualifiedwill be a mix of Male and female with majority aged 18 to 35 they are at thecareer development stage of their life cycle normally on an income 45k to 70kper annum. We would position these people very strongly in the “What is in itfor me”.

Group2- PM who has used a variety of tools and systemsover the years they will be pre disposed to one or more systems and has morethan likely been exposed to MSP. Usually in the 30 to 50 year old age rangewith extensive on the job experience.

KeyInfluencers- These are the people who while notactually utilizing the software need to receive information in the form ofreports etc from the system. They normally don’t have the capacity to say yesbut they most certainly can say no. They will have come from a PM or IT roleand have a strong understanding of the PM processes. Influencers will be 30 to50 years of age they are at the family development stage with strong demandsfrom work and family predominantly male but not exclusively. They would bedegree qualified and possibly have completed or looking at additional studies. Therewill be an emphasis on getting the job done right. They are very time poor and hardto communicate with and engage. While being time poor they have an affinitywith and understand the greater good.

DecisionMakers- These are our key decision makers whilethey may not have direct input into the system or processes they are at the endof the day the people who approve the expenditure.

There is a huge demand for this person’stime with a multitude of people from internal employees and management,suppliers, customers, the community and potential suppliers. They are oftentravelling and going from one subject matter to another meeting after meeting.They will be at the stage where children are gaining some independents or leftthe home, career is stabilized and a clear path is formed. They are very directand deal in the facts and figures when it comes to decision making, they arenormally highly educated to the MBA or Doctorate level. They will be driven byoutcomes not the process of getting there.

 

A consistent theme across this group isthe following.

Psychographics

·Values time and considers ittheir single most limited resource.

·Excited about accepting andusing innovative ideas and products always wants to be at the fore front.

·Value adding has priority overprice

·Consistent web users: preferinternet over magazines and newspapers

Behavior

·They are leaders in productselection and respond to the opinions of the ‘Industry Experts’ when makingpurchase decisions.

·This group will look to theinternet to acquire the information

·Will make an informed decisionto purchase after due consideration.

·This group can be a powerfulsales force resulting from the referral network they build and use

Hope this helps

Hi All

Sorry for the delay we are in the final stages of decisions, so sorry we have had people away from the office who need to be involved in the process.

We will submit individual questions to those in the running and let all of the people who didnt get through this time as to why shortly.

We would like to thank you all for your efforts and submissions.

Regards

Nigel Brask 

Industry/Entity Type

Business Management

Requirements
Must have
• The scope of the website is to provide a modern functional website that is easy to navigate and provides a range of products and services to meet the needs of our potential clients and current users.

Two potential groups of viewers exist:
1. Potential Clients and users from the Project management community these would be split into 3 distinct groups. ( Please refer to Page 20 Talvoro marketing Plan)
a. Project Managers
b. Project Directors
c. Business Managers
2. Current Talvoro Users

The goal of website is to engage with the project management community reinforcing the Talvoro Brand as Software with Service the key ethos should be around the company being thought leaders and industry experts with a strong commitment to clients and the success of their Portfolio/Program Management Office

Maintaining a modern and user friendly site is of the highest importance in order to hold users attention and guide the viewer to information that will lead to a decision to pursue accreditation and association with the Talvoro Brand

We would like to guide potential clients to want to engage with us in assisting them to understand their current position in the P3M3 maturity model and to use us as a source for information and guidance.

Benefits for using the site should include:
• Information from a broad spectrum of Project Management professionals and recognized industry experts.
• Information on the Talvoro Product and Services
• Timely and up to date information that encourages readers to return to the site
• Call to action, and plans for potential users of Talvoro software.
• Demonstrate the benefits of accreditation and Call to action for current users to gain accreditation.
• Call to action for attending monthly webinars
• Ability to review past webinars, whitepapers etc.

```html
<!DOCTYPE html>
<html lang="en">
<head>
<meta charset="utf-8">
<title>Talvoro</title>
<link href="https://fonts.googleapis.com/css2?family=Open+Sans:wght@400;600;700&display=swap" rel="stylesheet">
<style>
:root{
  --ink:#2b2b2b;
  --dark:#333333;
  --darker:#232323;
  --orange:#f36a1f;
  --orange-light:#f7923f;
  --grey-text:#6f6f6f;
  --line:#dedede;
  --white:#ffffff;
  --footer:#2f2f2f;
  --footer-text:#bdbdbd;
}
*{box-sizing:border-box;margin:0;padding:0}
html,body{width:865px;height:1200px;overflow:hidden}
body{font-family:"Open Sans",Arial,sans-serif;color:var(--ink);background:var(--white);position:relative}
a{color:inherit;text-decoration:none}

.site-header{position:absolute;top:0;left:0;width:865px;height:130px;background:linear-gradient(#3a3a3a,#2a2a2a)}
.util-nav{position:absolute;top:8px;right:40px;display:flex;gap:16px;font-size:11px;color:#cfcfcf}
.brand{position:absolute;left:40px;top:34px;display:flex;align-items:center;gap:10px}
.brand-mark{width:18px;height:18px;background:var(--orange)}
.brand-name{font-size:40px;font-weight:700;color:var(--white);line-height:1}
.main-nav{position:absolute;right:40px;top:74px;display:flex;gap:4px;font-size:12px;color:#e6e6e6}
.main-nav a{padding:7px 11px}
.main-nav a.active{background:var(--orange);color:var(--white)}

.hero{position:absolute;top:130px;left:0;width:865px;height:300px;background:linear-gradient(135deg,var(--orange) 0%,var(--orange-light) 60%,var(--orange) 100%)}
.hero-visual{position:absolute;left:115px;top:30px;width:285px;height:235px;background:linear-gradient(#e9eef3,#b9c3cc);border-radius:6px}
.hero-copy{position:absolute;left:465px;top:82px;width:345px;color:var(--white)}
.hero-copy h1{font-size:20px;font-weight:400;margin-bottom:10px;white-space:nowrap}
.hero-copy p{font-size:11px;line-height:1.55;color:#fde3d1}
.btn-light{display:inline-block;margin-top:16px;padding:6px 14px;background:var(--white);color:var(--ink);font-size:11px;font-weight:700;border-radius:2px}
.slider-dots{position:absolute;right:40px;bottom:14px;display:flex;gap:5px}
.slider-dots span{width:7px;height:7px;border-radius:50%;background:#fbc8a5}
.slider-dots span.on{background:var(--white)}

.intro{position:absolute;top:465px;left:0;width:865px;text-align:center}
.intro h2{font-size:20px;font-weight:600;margin-bottom:14px}
.intro p{width:620px;margin:0 auto;font-size:11px;line-height:1.6;color:var(--grey-text)}
.intro-actions{margin-top:22px;display:flex;justify-content:center;gap:14px}
.btn-dark{display:inline-block;padding:7px 18px;background:var(--darker);color:var(--white);font-size:11px;font-weight:700;border-radius:2px;white-space:nowrap}

.features{position:absolute;top:650px;left:60px;width:745px;display:flex;gap:15px}
.feature-card{flex:1;height:180px;border:1px solid var(--line);box-shadow:0 2px 4px rgba(0,0,0,.08);text-align:center;padding-top:36px;position:relative;background:var(--white)}
.feature-icon{position:absolute;top:-26px;left:50%;margin-left:-26px;width:52px;height:52px;border-radius:50%;background:var(--dark);border:3px solid var(--white);box-shadow:0 0 0 1px var(--line);display:flex;align-items:center;justify-content:center}
.feature-card h3{font-size:12px;font-weight:600;margin-bottom:3px;white-space:nowrap}
.feature-card h4{font-size:9px;font-weight:600;color:var(--grey-text);margin-bottom:9px}
.feature-card p{font-size:9px;line-height:1.5;color:var(--grey-text);padding:0 14px}
.feature-card .btn-dark{position:absolute;bottom:12px;left:50%;transform:translateX(-50%);padding:5px 14px;font-size:10px}

.clients{position:absolute;top:870px;left:60px;width:745px;border-top:1px solid var(--line);padding-top:18px}
.clients h2{font-size:15px;font-weight:600}
.clients-nav{position:absolute;right:0;top:22px;display:flex;gap:5px}
.clients-nav span{width:12px;height:12px;border-radius:50%;background:#cccccc}
.client-row{margin-top:28px;display:flex;justify-content:space-between;align-items:center}
.client{display:flex;align-items:center;gap:6px;font-size:16px;font-weight:700;color:#555555}
.client i{width:12px;height:12px;background:#888888;display:block}

.site-footer{position:absolute;top:1018px;left:0;width:865px;height:182px;background:var(--footer);color:var(--footer-text);font-size:10px}
.footer-cols{position:absolute;left:60px;top:20px;width:745px;display:flex}
.footer-col{width:105px}
.footer-col h5{font-size:11px;color:var(--white);font-weight:600;margin-bottom:8px}
.footer-col li{list-style:none;margin-bottom:5px}
.newsletter{width:215px}
.newsletter input{display:block;width:140px;height:18px;margin-bottom:6px;border:0;background:#f4f4f4;font-family:inherit;font-size:9px;padding:0 6px}
.newsletter .submit{display:inline-block;padding:3px 10px;background:#3b6fc4;color:var(--white);font-size:9px}
.social li{display:flex;align-items:center;gap:6px;margin-bottom:7px}
.social i{width:14px;height:14px;border-radius:3px;background:#555;display:block}
.copyright{position:absolute;bottom:0;left:0;width:865px;height:26px;background:#1e1e1e;padding:7px 60px;font-size:9px;color:#9a9a9a}
</style>
</head>
<body>

<header class="site-header">
  <nav class="util-nav"><a>Tours</a><a>Features</a><a>Pricing</a><a>Signup</a><a>Login</a></nav>
  <div class="brand"><span class="brand-mark"></span><span class="brand-name">Talvoro</span></div>
  <nav class="main-nav">
    <a class="active">Home</a><a>FAQ</a><a>Download</a><a>Support &amp; Training</a><a>Customers</a><a>About Us</a><a>Contact</a>
  </nav>
</header>

<section class="hero">
  <div class="hero-visual" role="img" aria-label="Desktop monitor showing the project management software dashboard"></div>
  <div class="hero-copy">
    <h1>Per an putent audiam adolescens</h1>
    <p>Mollis sed diam dolore magna aliquam erat volutpat ut wisi enim ad minim veniam, quis nostrud exerci tation ullamcorper suscipit lobortis nisl ut aliquip commodo consequat.</p>
    <a class="btn-light">FREE TRAIL</a>
  </div>
  <div class="slider-dots"><span class="on"></span><span></span><span></span><span></span></div>
</section>

<section class="intro">
  <h2>Powerful hosted project time and status collections</h2>
  <p>Claritas est etiam processus dynamicus, qui sequitur mutationem consuetudium lectorum. Mirum est notare quam littera gothica, quam nunc putamus parum claram, anteposuerit litterarum formas humanitatis per seacula quarta decima et quinta decima.</p>
  <div class="intro-actions"><a class="btn-dark">DOWNLOAD NOW</a><a class="btn-dark">TAKE A TOUR</a></div>
</section>

<section class="features">
  <article class="feature-card">
    <div class="feature-icon"><svg width="24" height="24" viewBox="0 0 24 24"><rect x="3" y="7" width="18" height="13" rx="2" fill="none" stroke="#fff" stroke-width="2"/><path d="M9 7V4h6v3" fill="none" stroke="#fff" stroke-width="2"/></svg></div>
    <h3>Project Management</h3><h4>Aenean nonummy hendrerit</h4>
    <p>Praesent vestibulum molestie lacus, nonummy hendrerit.</p>
    <a class="btn-dark">READ MORE</a>
  </article>
  <article class="feature-card">
    <div class="feature-icon"><svg width="24" height="24" viewBox="0 0 24 24"><circle cx="12" cy="12" r="9" fill="none" stroke="#fff" stroke-width="2"/><path d="M12 7v5l4 2" fill="none" stroke="#fff" stroke-width="2"/></svg></div>
    <h3>Timesheets</h3><h4>Aenean nonummy hendrerit</h4>
    <p>Praesent vestibulum molestie lacus, nonummy hendrerit.</p>
    <a class="btn-dark">READ MORE</a>
  </article>
  <article class="feature-card">
    <div class="feature-icon"><svg width="24" height="24" viewBox="0 0 24 24"><circle cx="9" cy="8" r="3" fill="#fff"/><circle cx="16" cy="9" r="2.5" fill="#fff"/><path d="M3 19c0-4 3-6 6-6s6 2 6 6z" fill="#fff"/><path d="M15 13c3 0 6 2 6 5h-5" fill="#fff"/></svg></div>
    <h3>Resource Management</h3><h4>Aenean nonummy hendrerit</h4>
    <p>Praesent vestibulum molestie lacus, nonummy hendrerit.</p>
    <a class="btn-dark">READ MORE</a>
  </article>
  <article class="feature-card">
    <div class="feature-icon"><svg width="24" height="24" viewBox="0 0 24 24"><path d="M12 3l10 18H2z" fill="none" stroke="#fff" stroke-width="2"/><path d="M12 10v5M12 17v2" stroke="#fff" stroke-width="2"/></svg></div>
    <h3>Issue Management</h3><h4>Aenean nonummy hendrerit</h4>
    <p>Praesent vestibulum molestie lacus, nonummy hendrerit.</p>
    <a class="btn-dark">READ MORE</a>
  </article>
</section>

<section class="clients">
  <h2>Our Clients</h2>
  <div class="clients-nav"><span></span><span></span></div>
  <div class="client-row">
    <div class="client"><i></i>Orvanta</div>
    <div class="client">Swiftmere</div>
    <div class="client"><i></i>Dralvex</div>
    <div class="client">Lumacore</div>
    <div class="client"><i></i>Keystrand</div>
  </div>
</section>

<footer class="site-footer">
  <div class="footer-cols">
    <div class="footer-col"><h5>Home</h5><ul><li>FAQ</li><li>Support &amp; Training</li><li>Contact Us</li></ul></div>
    <div class="footer-col"><h5>Tour</h5><ul><li>Features</li><li>Pricing</li><li>Sign up</li></ul></div>
    <div class="footer-col"><h5>Careers</h5><ul><li>Privacy Policy</li><li>Terms of Sub</li><li>Sitemap</li></ul></div>
    <div class="footer-col newsletter"><h5>Newsletter Signup</h5>
      <input type="text" placeholder="Name"><input type="text" placeholder="Email ID">
      <span class="submit">SUBMIT</span>
    </div>
    <div class="footer-col social"><h5>Connect with us</h5>
      <ul><li><i></i>Chatterbox</li><li><i></i>Pinhaven</li><li><i></i>Skylark</li></ul>
    </div>
  </div>
  <div class="copyright">Copyright 2013. All Rights Reserved.</div>
</footer>

</body>
</html>
```